Varnick Earthworks and Septic needs a flyer to submit to contractors to offer our services

I need a sleek profession one page full color high gloss document showcasing our services to give to Mobile Home Companies and contractors that need our services.

Target Market(s)

Home Builders. Mobile Home Salesmen. People Building new homes.

Industry/Entity Type

Construction

Font styles to use
Serif
Sans Serif

Requirements
Must have
• Phone Number. Email address. Logo. Services offered: Mobile Home Pads, Meter Pole Placement and Connection, Waterline Connection, On Site Septic System Installs
Should not have
• Jokes, Nothing trying to be cute

```html
<!DOCTYPE html>
<html lang="en">
<head>
<meta charset="UTF-8">
<title>Varnick Earthworks and Septic – Services Flyer</title>
<link rel="stylesheet" href="https://fonts.googleapis.com/css2?family=Montserrat:wght@400;500;700;800&family=Russo+One&display=swap">
<style>
  :root {
    --sky-top: #2f63d6;
    --sky-low: #8db6e6;
    --mist-top: #d4e3f1;
    --mist-low: #e6ecee;
    --earth: #7a5a3e;
    --clay: #9c5236;
    --sand: #b98a5e;
    --navy: #1c4f86;
    --service-red: #c1121b;
    --band-dark: #3a050b;
    --band-red: #d30a12;
    --white: #ffffff;
  }
  * { margin: 0; padding: 0; box-sizing: border-box; }
  html, body { width: 812px; height: 1200px; overflow: hidden; background: #a9a9a9; }
  .flyer {
    position: relative;
    width: 812px;
    height: 1200px;
    overflow: hidden;
    background: linear-gradient(180deg, var(--mist-top) 0%, var(--mist-low) 70%, #dfe6e4 100%);
    font-family: "Montserrat", Arial, sans-serif;
  }
  .hero-photo { position: absolute; left: 0; top: 0; width: 812px; height: 560px; }
  .brand-badge {
    position: absolute; left: 36px; top: 42px;
    width: 132px; height: 132px; border-radius: 50%;
    background: var(--white);
    display: flex; align-items: center; justify-content: center; text-align: center;
    padding: 18px;
    font-weight: 800; font-size: 15px; line-height: 1.2;
    color: var(--navy);
  }
  .job-photo {
    position: absolute; width: 188px; height: 188px; border-radius: 50%;
    border: 4px solid var(--white);
  }
  .job-photo--risers { left: 56px; top: 381px; background: var(--earth); }
  .job-photo--pad { left: 312px; top: 476px; background: var(--clay); }
  .job-photo--excavator { left: 572px; top: 381px; background: var(--sand); }
  .services-title {
    position: absolute; left: 201px; top: 704px; width: 410px; height: 50px;
    border-radius: 8px; background: var(--navy); color: var(--white);
    font-family: "Russo One", "Arial Black", sans-serif; font-size: 31px; font-weight: 400; letter-spacing: 1px;
    display: flex; align-items: center; justify-content: center;
  }
  .service-list { position: absolute; left: 0; top: 787px; width: 812px; list-style: none; text-align: center; }
  .service-list li {
    color: var(--service-red); font-weight: 500; font-size: 26px;
    height: 50px; line-height: 38px;
  }
  .service-list li:last-child { padding-left: 14px; margin-top: 6px; }
  .contact-email {
    position: absolute; left: 118px; top: 1023px; width: 592px; height: 44px;
    background: rgba(236, 242, 246, 0.9);
    color: var(--navy); font-weight: 500; font-size: 28px;
    display: flex; align-items: center; justify-content: center;
  }
  .phone-band {
    position: absolute; left: 0; top: 1084px; width: 812px; height: 116px;
    background: linear-gradient(90deg, var(--band-dark) 0%, #8e0a10 45%, var(--band-red) 100%);
    color: var(--white); font-weight: 800; font-size: 104px; line-height: 1; letter-spacing: -1px;
    display: flex; align-items: center; justify-content: center;
  }
</style>
</head>
<body>
  <main class="flyer">
    <svg class="hero-photo" viewBox="0 0 812 560" role="img" aria-label="Photo of a concrete septic tank being lifted by a crane over a dug site in an open field under blue sky">
      <defs>
        <linearGradient id="heroTones" x1="0" y1="0" x2="0" y2="1">
          <stop offset="0" stop-color="#2f63d6"/>
          <stop offset="1" stop-color="#8db6e6"/>
        </linearGradient>
      </defs>
      <path d="M0 0 H812 V420 C700 520 560 555 410 555 C260 555 120 500 0 375 Z" fill="url(#heroTones)"/>
    </svg>

    <div class="brand-badge">Varnick Earthworks and Septic</div>

    <div class="job-photo job-photo--risers" role="img" aria-label="Photo of green septic riser lids set in bare soil"></div>
    <div class="job-photo job-photo--pad" role="img" aria-label="Photo of a graded red-dirt mobile home pad with a septic lid"></div>
    <div class="job-photo job-photo--excavator" role="img" aria-label="Photo of an excavator digging beside a septic tank installation"></div>

    <h2 class="services-title">SERVICES OFFERED</h2>
    <ul class="service-list">
      <li>Mobile Home Pads</li>
      <li>Waterline Connection</li>
      <li>On Site Septic System Installs</li>
      <li>Meter Pole Placement and Connection</li>
    </ul>

    <p class="contact-email">info@varnickearthworks.com</p>
    <p class="phone-band">555.014.2786</p>
  </main>
</body>
</html>
```